Private lender of mortgages and rent to own housing

need a website that reflects real estate especially mortgage lending and rent to own houses..
Sections as follows
Home About Types of mortgages Rent to own Contact us
Target Market(s)
consumers who require non traditonal mortgages
Industry/Entity Type
Mortgage
Coding
Coded - Design and coding required
Number of Pages Required
4 page
Font styles to use
Sans Serif
Colors
Designer to choose colors to be used in the design.
Requirements
Must have
- background pictures on pages. with nice picture on homepage of houses or a community
Nice to have
- contact us form i supplied a ink to

```html
<!DOCTYPE html>
<html lang="en">
<head>
<meta charset="utf-8">
<title>Harborline Lending Group – Private Mortgages &amp; Rent to Own</title>
<link href="https://fonts.googleapis.com/css2?family=Montserrat:wght@300;400;500;600;700&family=Open+Sans:wght@400;600&display=swap" rel="stylesheet">
<style>
:root{
  --navy:#2b2a6e;
  --blue:#0a57a3;
  --sky:#1b8fd6;
  --accent:#1a86cc;
  --ink:#333;
  --muted:#7a7a7a;
  --pale:#f1f1f1;
  --footer:#5e5e5e;
  --white:#fff;
}
*{margin:0;padding:0;box-sizing:border-box}
html,body{width:733px;height:1200px;overflow:hidden}
body{position:relative;font-family:"Open Sans",sans-serif;color:var(--ink);
  background:linear-gradient(180deg,#c9cdc9 0%,#d8d9d6 40%,#cfd2cc 75%,#c4c6c2 100%)}
.abs{position:absolute}
.backdrop-left,.backdrop-right{position:absolute;top:240px;height:828px}
.backdrop-left{left:0;width:154px;background:linear-gradient(180deg,#cdd4cc,#d6d8d2 45%,#c7cbc0)}
.backdrop-right{left:578px;width:155px;background:linear-gradient(180deg,#d5d7d4,#dcdcd9 50%,#cfd0c9)}

/* header */
.site-header{left:154px;top:0;width:579px;height:34px}
.header-bar{position:absolute;left:0;top:0;width:579px;height:34px}
.brand{position:absolute;left:30px;top:20px;font:700 5.2px "Montserrat",sans-serif;color:var(--navy);white-space:nowrap;letter-spacing:.1px}
.brand-mark{display:inline-block;width:5px;height:5px;border-radius:50%;background:var(--navy);margin-right:3px;vertical-align:-.5px}
.call{position:absolute;right:191px;top:8px;font:600 7px "Montserrat",sans-serif;color:var(--white);white-space:nowrap}
.nav{position:absolute;left:144px;top:21px;display:flex;white-space:nowrap;font:400 5.6px "Montserrat",sans-serif;color:var(--white)}
.nav span{padding:0 4.5px}
.nav .sep{padding:0;opacity:.8}

/* hero */
.hero{left:0;top:0;width:733px;height:240px;z-index:-1;
  background:linear-gradient(180deg,#6f6a68 0%,#8a7f74 30%,#6a5a47 60%,#3d4638 100%)}
.hero-title{left:190px;top:108px;font:600 12px/14px "Montserrat",sans-serif;color:var(--white)}
.hero-btn{left:190px;top:149px;width:73px;height:15px;background:var(--accent);color:var(--white);font:600 5.5px/15px "Montserrat",sans-serif;text-align:center}
.hero-arrow{top:130px;width:8px;height:14px}

/* about */
.about{left:154px;top:240px;width:243px;height:186px;background:var(--white)}
.about-photo{left:397px;top:240px;width:145px;height:186px;background:linear-gradient(160deg,#a9b9c7 0%,#9a6a43 40%,#5d7a3d 75%,#6b8e3c 100%)}
.section-label{font:300 11px "Montserrat",sans-serif;color:var(--ink)}
.section-label b{font-weight:600;color:var(--accent)}
.about .section-label{position:absolute;left:37px;top:36px}
.body-text{font:400 5.6px/8.3px "Open Sans",sans-serif;color:var(--muted)}
.about .body-text{position:absolute;left:37px;width:185px}
.outline-btn{position:absolute;left:37px;top:148px;width:62px;height:16px;border:1px solid var(--accent);font:500 5.5px/14px "Montserrat",sans-serif;color:var(--ink);text-align:center}

/* mortgage types */
.types{left:154px;top:426px;width:424px;height:131px;background:var(--blue)}
.types-title{position:absolute;left:0;width:424px;top:21px;text-align:center;font:300 11px "Montserrat",sans-serif;color:var(--white)}
.types-title b{font-weight:600}
.type-tab{position:absolute;top:54px;width:117px;height:77px;text-align:center;color:var(--white);font:600 7px "Montserrat",sans-serif}
.type-tab svg{display:block;margin:14px auto 6px}
.type-tab.active{background:var(--sky)}
.tab-pointer{left:359px;top:557px;width:0;height:0;border-left:8px solid transparent;border-right:8px solid transparent;border-top:8px solid var(--sky)}

.bridge{left:154px;top:557px;width:424px;height:216px;background:var(--pale)}
.bridge-title{position:absolute;top:24px;width:424px;text-align:center;font:600 11px "Montserrat",sans-serif;color:var(--accent)}
.bridge-lead{position:absolute;left:36px;top:41px;width:352px;text-align:center}
.rule{position:absolute;left:82px;top:83px;width:260px;height:1px;background:#d4d4d4}
.col-head{position:absolute;top:97px;font:600 7px "Montserrat",sans-serif;color:var(--ink)}
.col-head::before{content:"";display:inline-block;width:13px;height:1px;background:var(--ink);vertical-align:2px;margin-right:6px}
.col-text{position:absolute;top:112px;width:156px}
.col-divider{position:absolute;left:212px;top:97px;width:1px;height:82px;background:#d4d4d4}

/* rent to own */
.rent{left:154px;top:773px;width:424px;height:295px;background:var(--white)}
.rent-title{position:absolute;top:20px;width:424px;text-align:center;font:300 11.5px "Montserrat",sans-serif;color:var(--ink)}
.rent-title b{font-weight:600;color:var(--accent)}
.rent-sub{position:absolute;top:57px;width:424px;text-align:center;font:600 7px "Montserrat",sans-serif;letter-spacing:.3px}
.rent-lead{position:absolute;left:40px;top:72px;width:344px;text-align:center}
.feature{position:absolute;width:190px;height:60px}
.feature .icon{position:absolute;left:0;top:0;width:38px;height:38px;border-radius:50%;border:1px solid #9ccbe9;display:flex;align-items:center;justify-content:center;background:var(--white)}
.feature .icon.filled{background:var(--accent);border-color:var(--accent)}
.feature h3{position:absolute;left:49px;top:3px;font:500 7.5px "Montserrat",sans-serif;color:var(--ink)}
.feature p{position:absolute;left:49px;top:16px;width:120px;font:400 5.4px/8.2px "Open Sans",sans-serif;color:var(--muted)}
.feature .more{position:absolute;left:49px;top:50px;font:600 5.5px "Montserrat",sans-serif;color:var(--ink)}
.feature .more.hot{color:var(--accent)}
.apply-btn{position:absolute;left:126px;top:257px;width:173px;height:15px;background:var(--accent);color:var(--white);font:600 5.5px/15px "Montserrat",sans-serif;text-align:center}

/* footer */
.site-footer{left:0;top:1068px;width:733px;height:132px;background:var(--footer);color:var(--white)}
.contact-item{position:absolute;top:20px;width:120px;text-align:center}
.contact-item svg{display:block;margin:0 auto 6px}
.contact-item strong{display:block;font:600 7px/9px "Montserrat",sans-serif}
.contact-item span{display:block;font:400 5.5px/7.5px "Open Sans",sans-serif}
.contact-item a{display:block;color:var(--white);font:400 5.5px/7px "Open Sans",sans-serif;text-decoration:underline}
.foot-rule{position:absolute;left:190px;top:81px;width:352px;height:1px;background:#7c7c7c}
.foot-nav{position:absolute;left:190px;top:88px;width:352px;display:flex;justify-content:center;white-space:nowrap;font:400 5.5px "Montserrat",sans-serif}
.foot-nav span{padding:0 6px}
.foot-nav .current{color:var(--accent)}
.copyright{position:absolute;left:190px;top:113px;font:400 5.3px "Open Sans",sans-serif;color:#e6e6e6;white-space:nowrap}
.copyright u{text-decoration:underline}
.social{position:absolute;left:430px;top:108px;display:flex;gap:5px}
.social i{display:block;width:15px;height:15px;border-radius:50%;border:1px solid #9b9b9b}
.social i.on{background:var(--accent);border-color:var(--accent)}
.to-top{position:absolute;left:524px;top:108px;width:15px;height:15px;border-radius:50%;border:1px solid var(--accent)}
</style>
</head>
<body>

<div class="abs hero" role="img" aria-label="Dusk photograph of a modern stone and timber house with a lit patio and pool"></div>
<div class="backdrop-left" role="img" aria-label="Faded photograph of suburban trees and a garden path"></div>
<div class="backdrop-right" role="img" aria-label="Faded photograph of a grey clapboard family house"></div>

<header class="abs site-header">
  <svg class="header-bar" viewBox="0 0 579 34" width="579" height="34">
    <rect x="0" y="0" width="579" height="34" fill="#2b2a6e"/>
    <polygon points="0,0 144,0 120,34 0,34" fill="#fff"/>
  </svg>
  <div class="brand"><span class="brand-mark"></span>HARBORLINE LENDING GROUP</div>
  <div class="call">Call Us: 555 - 014 - 2290</div>
  <nav class="nav">
    <span>Home</span><span class="sep">|</span><span>About us</span><span class="sep">|</span><span>Types of mortgages</span><span class="sep">|</span><span>Rent to Own</span><span class="sep">|</span><span>FAQ</span><span class="sep">|</span><span>Contact us</span>
  </nav>
</header>

<svg class="abs hero-arrow" style="left:111px" viewBox="0 0 8 14"><polyline points="7,1 1,7 7,13" fill="none" stroke="#fff" stroke-width="1"/></svg>
<svg class="abs hero-arrow" style="left:616px" viewBox="0 0 8 14"><polyline points="1,1 7,7 1,13" fill="none" stroke="#fff" stroke-width="1"/></svg>

<h1 class="abs hero-title">Private Lender of Mortgages and<br>Rent to Own Housing</h1>
<div class="abs hero-btn">Rent to Own a Home</div>

<section class="abs about">
  <h2 class="section-label">About <b>Us</b></h2>
  <p class="body-text" style="top:61px">Harborline Lending Group is a private lender of 1st,2nd, construction and bridge mortgages in Pinecrest County area. HLG offers a wide array of financing options to provide assistance to those of you that do not meet the bank's criteria.</p>
  <p class="body-text" style="top:110px">The reasons could range from bruised credit to inability to provide the banks with the required documentation to meet income qualification guidelines or...</p>
  <div class="outline-btn">Discover More</div>
</section>
<div class="abs about-photo" role="img" aria-label="Photograph of a timber-clad house with a landscaped stone garden and lawn"></div>

<section class="abs types">
  <h2 class="types-title">Types of <b>Mortgages</b></h2>
  <div class="type-tab" style="left:36px">
    <svg width="38" height="34" viewBox="0 0 38 34"><path d="M17 3 A15 15 0 1 0 32 18 L17 18 Z" fill="#fff"/><circle cx="26" cy="12" r="9" fill="none" stroke="#fff" stroke-width="2"/><text x="26" y="16" font-size="11" font-weight="700" fill="#fff" text-anchor="middle" font-family="Montserrat,sans-serif">$</text></svg>
    Debt Consolidation
  </div>
  <div class="type-tab active" style="left:154px">
    <svg width="38" height="34" viewBox="0 0 38 34"><polygon points="19,2 2,17 6,17 6,32 32,32 32,17 36,17" fill="#fff"/><rect x="15" y="21" width="8" height="11" fill="#1b8fd6"/></svg>
    Bridge Financing
  </div>
  <div class="type-tab" style="left:272px">
    <svg width="40" height="34" viewBox="0 0 40 34"><polygon points="14,4 2,15 5,15 5,32 23,32 23,15 26,15" fill="#fff"/><rect x="11" y="22" width="6" height="10" fill="#0a57a3"/><polyline points="20,28 27,20 31,24 38,12" fill="none" stroke="#fff" stroke-width="3"/><polygon points="34,10 39,9 38,15" fill="#fff"/></svg>
    Equity take out
  </div>
</section>
<div class="abs tab-pointer"></div>

<section class="abs bridge">
  <h2 class="bridge-title">Bridge Financing</h2>
  <p class="body-text bridge-lead">Are you or your client looking forward to moving into that new property you just purchased, but your possession date is earlier than the sale of your current property? Often, possession dates don't align in a way that is most convenient, and our bridge financing option will provide...</p>
  <div class="rule"></div>
  <h3 class="col-head" style="left:36px">Problem</h3>
  <p class="body-text col-text" style="left:36px">Are you or your client looking forward to moving into that new property you just purchased, but your Loans are often too short term You don't want to lose the sales of your property while waiting for financing Existing lenders are not willing or able to bridge the purchase with your existing equity Limited and restrictive conditions cause penalties at traditional financial institutions Your house is listed but hasn't sold yet.</p>
  <div class="col-divider"></div>
  <h3 class="col-head" style="left:229px">Solution</h3>
  <p class="body-text col-text" style="left:229px">We can help you close the sale of your purchase before the property you are moving out of sells, or before its possession date if it is sold. We offer a short term loan to bridge the gap for you, allowing a less stressful transition between homes. We can also help you take advantage of your prepayment privileges on the house you are selling to help reduce your prepayment penalty.</p>
</section>

<section class="abs rent">
  <h2 class="rent-title">Rent to <b>Own a Home</b></h2>
  <h3 class="rent-sub">We Can Put You in Your Own Home Today</h3>
  <p class="body-text rent-lead">We know life sometimes delivers challenges and it can be hard to get back on track once you have dealt with challenges. Maybe you have been through a divorce, bankruptcy, consumer proposal, loss of job, work place injury, new to the country, self-employed or some credit related challenges...</p>

  <div class="feature" style="left:36px;top:118px">
    <div class="icon"><svg width="18" height="20" viewBox="0 0 18 20"><rect x="3" y="1" width="10" height="17" rx="1.5" fill="none" stroke="#333" stroke-width="1.4"/><text x="8" y="12" font-size="7" font-weight="700" text-anchor="middle" fill="#333" font-family="Montserrat,sans-serif">$</text></svg></div>
    <h3>Down Payment</h3>
    <p>We know life sometimes delivers challenges and it can be hard to get...</p>
    <span class="more">Read More</span>
  </div>
  <div class="feature" style="left:242px;top:118px">
    <div class="icon"><svg width="20" height="18" viewBox="0 0 20 18"><polyline points="1,9 9,2 17,9" fill="none" stroke="#333" stroke-width="1.5"/><rect x="4" y="8" width="10" height="9" fill="none" stroke="#333" stroke-width="1.4"/><circle cx="15" cy="5" r="4" fill="#fff" stroke="#333"/><text x="15" y="7.5" font-size="6" font-weight="700" text-anchor="middle" fill="#333" font-family="Montserrat,sans-serif">$</text></svg></div>
    <h3>Household Income</h3>
    <p>Steady, provable household income that can support the price of.....</p>
    <span class="more hot">Read More</span>
  </div>
  <div class="feature" style="left:36px;top:189px">
    <div class="icon filled"><svg width="20" height="16" viewBox="0 0 20 16"><rect x="3" y="2" width="15" height="10" rx="1.5" fill="none" stroke="#fff" stroke-width="1.4"/><line x1="3" y1="5" x2="18" y2="5" stroke="#fff" stroke-width="1.5"/><rect x="1" y="8" width="7" height="6" fill="#fff"/></svg></div>
    <h3>Credit Report</h3>
    <p>Although your credit won't necessarily disqualify you from our rent to...</p>
    <span class="more">Read More</span>
  </div>
  <div class="feature" style="left:242px;top:189px">
    <div class="icon"><svg width="20" height="18" viewBox="0 0 20 18"><polyline points="2,9 10,2 18,9" fill="none" stroke="#333" stroke-width="1.5"/><rect x="5" y="8" width="10" height="9" fill="none" stroke="#333" stroke-width="1.4"/><polyline points="7,12 9,14 13,10" fill="none" stroke="#333" stroke-width="1.3"/></svg></div>
    <h3>Selecting a House</h3>
    <p>May not seem like a strong determining factor overall for qualifying for rent to ...</p>
    <span class="more">Read More</span>
  </div>
  <div class="apply-btn">Submit Application for Rent-To-Own A Home Program</div>
</section>

<footer class="abs site-footer">
  <div class="contact-item" style="left:188px">
    <svg width="16" height="18" viewBox="0 0 16 18"><path d="M4 1 L7 5 L5 7 C6 10 8 12 10 13 L12 11 L15 14 L13 17 C7 16 2 10 1 4 Z" fill="none" stroke="#fff" stroke-width="1.1"/></svg>
    <strong>555-014-2290</strong>
    <a>Email Us</a>
  </div>
  <div class="contact-item" style="left:306px">
    <svg width="14" height="18" viewBox="0 0 14 18"><path d="M7 17 C3 11 1 8 1 6 A6 6 0 0 1 13 6 C13 8 11 11 7 17 Z" fill="none" stroke="#fff" stroke-width="1.1"/><circle cx="7" cy="6" r="2" fill="none" stroke="#fff"/></svg>
    <span>4410 Cedar Ridge Rd.<br>Lakeview, ON 20418</span>
  </div>
  <div class="contact-item" style="left:424px">
    <svg width="14" height="18" viewBox="0 0 14 18"><path d="M3 5 A4 4 0 1 1 8 9 C7 10 7 11 7 13" fill="none" stroke="#fff" stroke-width="1.2"/><circle cx="7" cy="16.5" r="1" fill="#fff"/></svg>
    <strong>Need Help?</strong>
    <a>Contact Us</a>
  </div>
  <div class="foot-rule"></div>
  <nav class="foot-nav">
    <span class="current">Home</span><span>|</span><span>About us</span><span>|</span><span>Types of mortgages</span><span>|</span><span>Rent to Own</span><span>|</span><span>FAQ</span><span>|</span><span>Contact us</span>
  </nav>
  <p class="copyright">© 2017 True <u>Harborline Lending Group</u>. All right reserved</p>
  <div class="social"><i></i><i></i><i class="on"></i><i></i></div>
  <div class="to-top"><svg width="13" height="13" viewBox="0 0 13 13"><polyline points="3.5,7 6.5,4 9.5,7" fill="none" stroke="#1a86cc" stroke-width="1"/><line x1="6.5" y1="4" x2="6.5" y2="10" stroke="#1a86cc"/></svg></div>
</footer>

</body>
</html>
```